Orvel Crest Holdings Ltd
Creative Brief
Dara Kolby
COO
27B Hollin Row, London, E3 9TQ
dk@orvelcrest.co.uk
27b Hollin Row
Just the logo and the company's name on the green background

```html
<!DOCTYPE html>
<html lang="en">
<head>
<meta charset="utf-8">
<title>Orvel Crest Holdings Ltd — Business Card</title>
<link rel="stylesheet" href="https://fonts.googleapis.com/css2?family=Cormorant+Garamond:wght@500&family=Montserrat:wght@400;500;700&display=swap">
<style>
  :root {
    --canvas-bg: #e7e7e7;
    --olive-dark: #3e3f31;
    --gold: #c8a36a;
    --gold-light: #e2c595;
    --ink: #3a3b2e;
    --muted: #6d6d66;
    --card-white: #ffffff;
  }
  * { box-sizing: border-box; margin: 0; padding: 0; }
  html, body {
    width: 1200px; height: 901px; overflow: hidden;
    background: var(--canvas-bg);
  }
  .canvas { position: relative; width: 1200px; height: 901px; }

  .card {
    position: absolute; left: 300px; width: 600px; height: 410px;
    border-radius: 28px; overflow: hidden;
  }

  /* Back face */
  .card--back { top: 66px; background: var(--olive-dark); }
  .back-mark {
    position: absolute; left: 0; right: 0; top: 72px;
    display: flex; flex-direction: column; align-items: center;
  }
  .back-mark__circle {
    width: 190px; height: 190px; border-radius: 50%;
    border: 2px solid var(--gold);
  }
  .back-mark__name {
    margin-top: 26px;
    font-family: "Cormorant Garamond", serif; font-weight: 500;
    font-size: 30px; letter-spacing: 2px; color: var(--gold);
    text-transform: uppercase;
  }

  /* Front face */
  .card--front { top: 486px; background: var(--card-white); }
  .brand {
    position: absolute; left: 40px; top: 74px; width: 240px;
    display: flex; flex-direction: column; align-items: center;
  }
  .brand__circle {
    width: 128px; height: 128px; border-radius: 50%;
    border: 2px solid var(--gold);
  }
  .brand__name {
    margin-top: 14px; text-align: center;
    font-family: "Cormorant Garamond", serif; font-weight: 500;
    color: var(--gold); text-transform: uppercase; line-height: 1.05;
  }
  .brand__name-main { display: block; font-size: 40px; letter-spacing: 1px; }
  .brand__name-sub { display: block; font-size: 17px; letter-spacing: 1.5px; margin-top: 4px; }

  .divider {
    position: absolute; left: 299px; top: 74px; width: 2px; height: 214px;
    background: var(--olive-dark);
  }

  .person {
    position: absolute; left: 321px; top: 78px;
    font-family: "Montserrat", sans-serif; color: var(--ink);
  }
  .person__name { font-size: 26px; font-weight: 700; letter-spacing: 0.5px; text-transform: uppercase; }
  .person__role { font-size: 13px; font-weight: 500; color: var(--muted); margin-top: 2px; }
  .person__address { margin-top: 32px; font-size: 14px; line-height: 1.5; color: var(--muted); }

  .contacts {
    list-style: none; margin-top: 20px;
    font-size: 14px; color: var(--muted);
  }
  .contacts li { display: flex; align-items: center; gap: 10px; line-height: 1.65; }
  .contacts svg { width: 12px; height: 12px; fill: var(--gold); flex: none; }

  .card-band {
    position: absolute; left: 0; right: 0; bottom: 0; height: 22px;
    background: var(--olive-dark);
  }
  .card-accent {
    position: absolute; right: 0; bottom: 0; width: 150px; height: 36px;
    background: linear-gradient(90deg, var(--gold), var(--gold-light));
    clip-path: polygon(22% 0, 100% 0, 100% 100%, 0 100%);
  }
</style>
</head>
<body>
<main class="canvas">

  <section class="card card--back" aria-label="Card back">
    <div class="back-mark">
      <div class="back-mark__circle"></div>
      <p class="back-mark__name">Orvel Crest Holdings Ltd</p>
    </div>
  </section>

  <section class="card card--front" aria-label="Card front">
    <div class="brand">
      <div class="brand__circle"></div>
      <p class="brand__name">
        <span class="brand__name-main">Orvel Crest</span>
        <span class="brand__name-sub">Holdings Ltd</span>
      </p>
    </div>

    <div class="divider"></div>

    <div class="person">
      <h1 class="person__name">Dara Kolby</h1>
      <p class="person__role">COO</p>
      <p class="person__address">27B Hollin Row,<br>London, E3 9TQ</p>

      <ul class="contacts">
        <li>
          <svg viewBox="0 0 24 24"><path d="M6.6 10.8a15.1 15.1 0 0 0 6.6 6.6l2.2-2.2c.3-.3.7-.4 1-.2 1.1.4 2.3.6 3.6.6.6 0 1 .4 1 1V20c0 .6-.4 1-1 1A17 17 0 0 1 3 4c0-.6.4-1 1-1h3.5c.6 0 1 .4 1 1 0 1.3.2 2.5.6 3.6.1.3 0 .7-.2 1z"/></svg>
          +44 (0)20 7946 0312
        </li>
        <li>
          <svg viewBox="0 0 24 24"><rect x="6" y="1" width="12" height="22" rx="2"/></svg>
          +44 (0)77 0090 0461
        </li>
        <li>
          <svg viewBox="0 0 24 24"><path d="M2 5h20v14H2z M2 5l10 8 10-8" /></svg>
          dk@orvelcrest.co.uk
        </li>
        <li>
          <svg viewBox="0 0 24 24"><path d="M12 1a8 8 0 0 0-8 8c0 6 8 14 8 14s8-8 8-14a8 8 0 0 0-8-8zm0 11a3 3 0 1 1 0-6 3 3 0 0 1 0 6z"/></svg>
          27b Hollin Row
        </li>
      </ul>
    </div>

    <div class="card-band"></div>
    <div class="card-accent"></div>
  </section>

</main>
</body>
</html>
```